Kelvoro Global corporate slide deck

We are looking for a custom powerpoint template to use both internally and externally with clients and during trainings/presentations. Our customers/clients often include a lot of government agencies, and we specialize in forensics, biometrics, and identity intelligence.
Requirements:
• Title slide
• Section slide
• Title and content slide
• Every slide branded
• Every slide (other than title) includes slide number (x of y), title, and date
• Modern-looking but conservative
• Visually appealing
• Source Sans Pro font
• Call out boxes

The circle in our logo does not signify or mean anything in any way, but we also don't mind it being used as a design element. We also like pulling the blue to red gradient.
Ideally we do not want to use any images of people, but iconography is likely okay.

```html
<!DOCTYPE html>
<html lang="en">
<head>
<meta charset="utf-8">
<title>Kelvoro Global – Corporate Slide Deck</title>
<link rel="stylesheet" href="https://fonts.googleapis.com/css2?family=Exo+2:wght@700;800&family=Source+Sans+3:wght@300;400;600;700&display=swap">
<style>
:root{
  --navy:#2b2a73;
  --plum:#6a2668;
  --crimson:#c21f45;
  --ink:#2e2c6e;
  --grey:#6e6e86;
  --rule:#dccfa8;
  --paper:#ffffff;
  --deck-gradient:linear-gradient(90deg,var(--navy) 18%,var(--crimson) 100%);
}
*{box-sizing:border-box}
html,body{margin:0;width:1200px;height:3000px;overflow:hidden}
body{background:linear-gradient(180deg,#ffffff 0%,#ececef 28%,#f4f4f6 100%);font-family:'Source Sans 3',sans-serif}
.board{position:relative;width:1200px;height:3000px}

.board-brand{position:absolute;left:90px;top:96px;margin:0;font:700 52px 'Source Sans 3',sans-serif;color:var(--navy);letter-spacing:-.5px}

.slide{position:absolute;width:502px;height:282px;background:var(--paper);overflow:hidden;box-shadow:0 3px 9px rgba(20,20,50,.28)}
.stack .slide{transform:scale(.8);transform-origin:0 0;box-shadow:0 4px 14px rgba(20,20,50,.35)}
.slide.gradient{background:var(--deck-gradient)}

.band{position:absolute;top:0;left:0;right:0;height:9px;background:var(--deck-gradient)}
.heading{position:absolute;left:90px;top:44px;margin:0;font:700 20px 'Exo 2',sans-serif;color:var(--ink);text-transform:uppercase;letter-spacing:.3px;white-space:nowrap}
.copy{position:absolute;left:90px;top:72px;width:192px;margin:0;font-size:10px;line-height:1.3;color:var(--grey)}
.copy strong{color:var(--ink);font-weight:700}

.foot-brand{position:absolute;left:33px;top:253px;font:700 12px 'Source Sans 3',sans-serif;color:var(--navy)}
.foot-rule{position:absolute;left:90px;right:40px;top:262px;height:1px;background:var(--rule)}
.foot-date,.foot-tag,.foot-page{position:absolute;top:265px;font-size:6.5px;color:var(--grey)}
.foot-date{left:90px}
.foot-tag{left:163px;font-variant:small-caps;letter-spacing:.2px}
.foot-page{left:437px;color:var(--ink)}
.foot-page b{font-weight:700}

.photo{position:absolute}
.pill-left{border-radius:70px 0 0 70px}

.cover-brand{position:absolute;left:0;right:0;top:76px;text-align:center;font:700 36px 'Source Sans 3',sans-serif;color:#fff}
.cover-title{position:absolute;left:0;right:0;top:156px;margin:0;text-align:center;font:700 23px 'Exo 2',sans-serif;color:#fff;letter-spacing:.4px}
.cover-sub{position:absolute;left:0;right:0;top:190px;text-align:center;font-size:9px;color:#fff;font-variant:small-caps;letter-spacing:2.5px}
.cover-web{position:absolute;right:38px;top:253px;font:700 7px 'Source Sans 3',sans-serif;color:#fff;display:flex;align-items:center;gap:4px}
.dot{display:inline-block;width:8px;height:8px;border-radius:50%;background:#fff}

.section-field{position:absolute;left:0;top:0;right:0;height:236px;background:var(--deck-gradient)}
.section-title{position:absolute;left:91px;top:174px;margin:0;font:700 20px 'Exo 2',sans-serif;color:#fff}
.section-sub{position:absolute;left:91px;top:200px;font-size:9px;color:#fff;font-variant:small-caps;letter-spacing:2.2px}

.connect{position:absolute;top:0;left:0;right:0;height:28px;background:var(--deck-gradient);display:flex;align-items:center;justify-content:space-between;padding:0 40px 0 65px;color:#fff}
.connect .link{font:700 7px 'Source Sans 3',sans-serif;display:flex;align-items:center;gap:4px}
.connect .cta{font-size:11px;font-weight:300}

.member{position:absolute;width:120px;text-align:center}
.member.narrow{width:92px}
.portrait{margin:0 auto;border-radius:50%;background:linear-gradient(160deg,#c9c6cf,#6c6a7a)}
.member-name{margin-top:6px;font-size:10px;font-weight:700;color:var(--ink);line-height:1.1}
.member-role{font-size:10px;color:var(--grey);line-height:1.15}

.services{position:absolute;left:82px;top:88px;width:380px;display:grid;grid-template-columns:repeat(5,70px);row-gap:8px}
.service{text-align:center;font-size:9px;line-height:1.15;color:var(--grey)}
.service svg{display:block;margin:0 auto 5px}

.legend{position:absolute;left:306px;top:138px;list-style:none;margin:0;padding:0}
.legend li{font-size:7px;color:var(--grey);height:21px;display:flex;align-items:center;gap:6px}
.legend i{width:6px;height:6px;border-radius:50%;display:inline-block}

.vehicles{position:absolute;left:90px;top:118px;margin:0;padding:0;list-style:none;font-size:9.5px;font-weight:700;color:var(--ink);line-height:1.35}
.vehicles li::before{content:"• "}
</style>
</head>
<body>
<main class="board">

  <p class="board-brand">Kelvoro</p>

  <section class="stack">
    <article class="slide gradient" style="left:390px;top:84px">
      <div class="cover-brand">Kelvoro</div>
      <h2 class="cover-title">TITLE GOES HERE</h2>
      <div class="cover-sub">Subtitle goes here</div>
    </article>

    <article class="slide" style="left:470px;top:189px">
      <div class="connect"><span class="link"><i class="dot"></i>www.kelvoro-global.com</span><span class="cta">Connect with Us</span><span class="link"><i class="dot"></i>@kelvoro-global</span></div>
      <h2 class="heading" style="top:52px">Our Team</h2>
      <div class="member" style="left:67px;top:106px"><div class="portrait" role="img" aria-label="Team member portrait" style="width:76px;height:90px"></div><div class="member-name">Darren Holloway</div><div class="member-role">CEO</div></div>
      <div class="member" style="left:199px;top:106px"><div class="portrait" role="img" aria-label="Team member portrait" style="width:76px;height:90px"></div></div>
      <div class="member" style="left:328px;top:106px"><div class="portrait" role="img" aria-label="Team member portrait" style="width:76px;height:90px"></div></div>
    </article>

    <article class="slide" style="left:549px;top:294px">
      <div class="band"></div>
      <h2 class="heading">Our Vision</h2>
      <p class="copy" style="width:190px">We are a company of innovators who help our clients do things they have never done before, all while staying true to scientific and accreditation standards. As our company evolves to meet the challenges of tomorrow, we will remain committed.</p>
      <div class="photo" role="img" aria-label="Blue digital network visual" style="left:322px;top:34px;width:139px;height:200px;border-radius:70px 70px 0 70px;background:radial-gradient(circle at 40% 30%,#3f7ad6,#10286b 75%)"></div>
    </article>

    <article class="slide" style="left:628px;top:398px">
      <div class="band"></div>
      <h2 class="heading">What We Do</h2>
      <p class="copy">Our multidisciplinary team applies the power of biological science, physical science, IT, and analytic methods to solve the most challenging mission problems.</p>
      <div class="photo pill-left" role="img" aria-label="Fingerprint scan close-up" style="left:295px;top:79px;width:207px;height:140px;background:linear-gradient(100deg,#0f1a2a,#4a5a6a 55%,#b9b4ac)"></div>
    </article>

    <article class="slide gradient" style="left:707px;top:503px">
      <div class="cover-brand">Kelvoro</div>
      <h2 class="cover-title">TITLE GOES HERE</h2>
      <div class="cover-sub">Subtitle goes here</div>
    </article>
  </section>

  <section class="grid">

    <article class="slide gradient" style="left:90px;top:797px">
      <div class="cover-brand">Kelvoro</div>
      <h2 class="cover-title">TITLE GOES HERE</h2>
      <div class="cover-sub">Subtitle goes here</div>
      <div class="cover-web"><i class="dot"></i>www.kelvoro-global.com</div>
    </article>

    <article class="slide" style="left:608px;top:797px">
      <div class="band"></div>
      <h2 class="heading">About Us</h2>
      <p class="copy">Established over two decades ago, Kelvoro boasts a distinguished track record in addressing critical global missions encompassing Forensics, Biometrics, Weapons Technical and Identity Intelligence, CBRNE, CWMD, and Public Health initiatives. With a steadfast commitment to excellence, our seasoned team of experts consistently delivers exceptional solutions, reinforcing Kelvoro's status as a trusted partner in solving the world's most pressing challenges.</p>
      <div class="photo pill-left" role="img" aria-label="Laboratory scientists at work" style="left:295px;top:80px;width:207px;height:137px;background:linear-gradient(100deg,#cfd8e4,#e9edf2 45%,#8fa6c6)"></div>
      <div class="foot-brand">Kelvoro</div><div class="foot-rule"></div>
      <div class="foot-date">01/07/2024</div><div class="foot-tag">The Global Leader in Forensics, Biometrics, and Identity Intelligence</div><div class="foot-page"><b>2</b> of <b>30</b></div>
    </article>

    <article class="slide" style="left:90px;top:1095px">
      <div class="band"></div>
      <h2 class="heading">What We Do</h2>
      <p class="copy">Our multidisciplinary team applies the power of biological science, physical science, IT, and analytic methods to solve the most challenging mission problems. With a passion for our work and a commitment to innovation, we Always Deliver Exceptional!!</p>
      <div class="photo pill-left" role="img" aria-label="Fingerprint scan close-up" style="left:295px;top:79px;width:207px;height:140px;background:linear-gradient(100deg,#0f1a2a,#4a5a6a 55%,#b9b4ac)"></div>
      <div class="foot-brand">Kelvoro</div><div class="foot-rule"></div>
      <div class="foot-date">01/07/2024</div><div class="foot-tag">The Global Leader in Forensics, Biometrics, and Identity Intelligence</div><div class="foot-page"><b>3</b> of <b>30</b></div>
    </article>

    <article class="slide" style="left:608px;top:1095px">
      <div class="band"></div>
      <h2 class="heading">Our Services</h2>
      <div class="services">
        <div class="service"><svg width="34" height="34" viewBox="0 0 34 34"><circle cx="17" cy="17" r="17" fill="#2b2a73"/><rect x="10" y="11" width="14" height="12" fill="none" stroke="#fff" stroke-width="1.5"/><path d="M10 15h14M14 11v12M20 11v12" stroke="#fff" stroke-width="1"/></svg>Forensics</div>
        <div class="service"><svg width="34" height="34" viewBox="0 0 34 34"><circle cx="17" cy="17" r="17" fill="#2b2a73"/><ellipse cx="17" cy="17" rx="6" ry="8" fill="none" stroke="#fff" stroke-width="1.3"/><ellipse cx="17" cy="17" rx="3" ry="4.5" fill="none" stroke="#fff" stroke-width="1.3"/></svg>Biometrics</div>
        <div class="service"><svg width="34" height="34" viewBox="0 0 34 34"><circle cx="17" cy="17" r="17" fill="#2b2a73"/><rect x="10" y="9" width="14" height="16" rx="1" fill="none" stroke="#fff" stroke-width="1.5"/><path d="M13 14h8M13 18h8M13 22h5" stroke="#fff" stroke-width="1.2"/></svg>Genealogy</div>
        <div class="service"><svg width="34" height="34" viewBox="0 0 34 34"><circle cx="17" cy="17" r="17" fill="#2b2a73"/><circle cx="17" cy="15" r="6" fill="#fff"/><rect x="14.5" y="21" width="5" height="4" fill="#fff"/></svg>Technology Innovation</div>
        <div class="service"><svg width="34" height="34" viewBox="0 0 34 34"><circle cx="17" cy="17" r="17" fill="#2b2a73"/><path d="M8 17q9-9 18 0q-9 9-18 0z" fill="none" stroke="#fff" stroke-width="1.4"/><circle cx="17" cy="17" r="3" fill="#fff"/></svg>Identity and Weapons Technical Intelligence</div>
        <div class="service"><svg width="34" height="34" viewBox="0 0 34 34"><circle cx="17" cy="17" r="17" fill="#2b2a73"/><circle cx="17" cy="17" r="7" fill="none" stroke="#fff" stroke-width="1.5"/><path d="M11 21h12" stroke="#fff" stroke-width="1.5"/></svg>CWMD / CBRNE</div>
        <div class="service"><svg width="34" height="34" viewBox="0 0 34 34"><circle cx="17" cy="17" r="17" fill="#2b2a73"/><path d="M11 10h12v9q0 5-6 7q-6-2-6-7z" fill="none" stroke="#fff" stroke-width="1.4"/><path d="M13.5 17l2.5 2.5 4.5-5" fill="none" stroke="#fff" stroke-width="1.5"/></svg>Emergency Preparedness</div>
        <div class="service"><svg width="34" height="34" viewBox="0 0 34 34"><circle cx="17" cy="17" r="17" fill="#2b2a73"/><rect x="10" y="10" width="6" height="6" fill="none" stroke="#fff" stroke-width="1.3"/><rect x="18" y="18" width="6" height="6" fill="none" stroke="#fff" stroke-width="1.3"/><path d="M16 13h5v5" fill="none" stroke="#fff" stroke-width="1.3"/></svg>Laboratory Process Optimization</div>
        <div class="service"><svg width="34" height="34" viewBox="0 0 34 34"><circle cx="17" cy="17" r="17" fill="#2b2a73"/><rect x="11" y="9" width="12" height="16" fill="#fff"/><path d="M17 12v6M14 15h6" stroke="#2b2a73" stroke-width="1.8"/></svg>Medical and Public Health Preparedness</div>
      </div>
      <div class="foot-brand">Kelvoro</div><div class="foot-rule"></div>
      <div class="foot-date">01/07/2024</div><div class="foot-tag">The Global Leader in Forensics, Biometrics, and Identity Intelligence</div><div class="foot-page"><b>4</b> of <b>30</b></div>
    </article>

    <article class="slide" style="left:90px;top:1393px">
      <div class="band"></div>
      <h2 class="heading" style="top:106px">Our Mission</h2>
      <p class="copy" style="top:134px;width:200px">To blend science and technology to deliver innovative solutions for our client's most challenging missions</p>
      <div class="photo" role="img" aria-label="Scientist beside a robotic arm" style="left:324px;top:47px;width:136px;height:205px;border-radius:68px 68px 0 68px;background:linear-gradient(160deg,#8da0b8,#c8d1dc 55%,#6e7f94)"></div>
      <div class="foot-brand">Kelvoro</div><div class="foot-rule"></div>
      <div class="foot-date">01/07/2024</div><div class="foot-tag">The Global Leader in Forensics, Biometrics, and Identity Intelligence</div><div class="foot-page"><b>5</b> of <b>30</b></div>
    </article>

    <article class="slide" style="left:608px;top:1393px">
      <div class="band"></div>
      <h2 class="heading">Our Vision</h2>
      <p class="copy">We are a company of innovators who help our clients do things they have never done before, all while staying true to scientific and accreditation standards. As our company evolves to meet the challenges of tomorrow, we will remain committed to our original business philosophy: creating innovative, cost-effective, and reliable scientific and technical solutions guaranteed to work in the real world.</p>
      <div class="photo" role="img" aria-label="Blue digital network visual" style="left:322px;top:47px;width:139px;height:205px;border-radius:70px 70px 0 70px;background:radial-gradient(circle at 40% 30%,#3f7ad6,#10286b 75%)"></div>
      <div class="foot-brand">Kelvoro</div><div class="foot-rule"></div>
      <div class="foot-date">01/07/2024</div><div class="foot-tag">The Global Leader in Forensics, Biometrics, and Identity Intelligence</div><div class="foot-page"><b>6</b> of <b>30</b></div>
    </article>

    <article class="slide" style="left:90px;top:1692px">
      <div class="photo" role="img" aria-label="Team meeting around a desk with a laptop" style="left:0;top:0;width:502px;height:282px;background:linear-gradient(120deg,#d8c6b6,#ece3da 50%,#cdbfb4)"></div>
      <div class="band"></div>
      <h2 class="heading">Two Decades of Committement</h2>
      <p class="copy" style="width:275px">Kelvoro's leadership team is committed to building a company that empowers clients to achieve optimal performance in applying science and technology to identify people, substances, and threats. <strong>Our leadership team combines decades of experience with a deep commitment to hiring, nurturing, and retaining world-class scientific, technical, and professional talent.</strong></p>
      <div class="foot-brand">Kelvoro</div><div class="foot-rule"></div>
      <div class="foot-date">01/07/2024</div><div class="foot-tag">The Global Leader in Forensics, Biometrics, and Identity Intelligence</div><div class="foot-page"><b>11</b> of <b>30</b></div>
    </article>

    <article class="slide" style="left:608px;top:1692px">
      <div class="section-field"></div>
      <h2 class="section-title">SECTION TITLE HERE</h2>
      <div class="section-sub">Subtitle goes here</div>
      <div class="foot-brand">Kelvoro</div><div class="foot-rule"></div>
      <div class="foot-date">01/07/2024</div><div class="foot-tag">The Global Leader in Forensics, Biometrics, and Identity Intelligence</div><div class="foot-page"><b>12</b> of <b>30</b></div>
    </article>

    <article class="slide" style="left:90px;top:1990px">
      <div class="connect"><span class="link"><i class="dot"></i>www.kelvoro-global.com</span><span class="cta">Connect with Us</span><span class="link"><i class="dot"></i>@kelvoro-global</span></div>
      <h2 class="heading" style="top:52px">Our Team</h2>
      <div class="member" style="left:67px;top:96px"><div class="portrait" role="img" aria-label="Portrait of Darren Holloway" style="width:76px;height:96px"></div><div class="member-name">Darren Holloway</div><div class="member-role">CEO</div></div>
      <div class="member" style="left:199px;top:96px"><div class="portrait" role="img" aria-label="Portrait of Miriam Castell" style="width:76px;height:96px"></div><div class="member-name">Miriam Castell</div><div class="member-role">Chief Science Officer</div></div>
      <div class="member" style="left:328px;top:96px"><div class="portrait" role="img" aria-label="Portrait of Nolan P. Briggs" style="width:76px;height:96px"></div><div class="member-name">Nolan P. Briggs</div><div class="member-role">President</div></div>
      <div class="foot-brand">Kelvoro</div><div class="foot-rule"></div>
      <div class="foot-date">01/07/2024</div><div class="foot-tag">The Global Leader in Forensics, Biometrics, and Identity Intelligence</div><div class="foot-page"><b>19</b> of <b>30</b></div>
    </article>

    <article class="slide" style="left:608px;top:1990px">
      <div class="connect"><span class="link"><i class="dot"></i>www.kelvoro-global.com</span><span class="cta">Connect with Us</span><span class="link"><i class="dot"></i>@kelvoro-global</span></div>
      <h2 class="heading" style="top:52px">Our Team</h2>
      <div class="member narrow" style="left:80px;top:90px"><div class="portrait" role="img" aria-label="Portrait of Gavin Marsh" style="width:76px;height:96px"></div><div class="member-name">Gavin Marsh</div><div class="member-role">Director of<br>Intelligence</div></div>
      <div class="member narrow" style="left:179px;top:90px"><div class="portrait" role="img" aria-label="Portrait of Clara Winslow" style="width:76px;height:96px"></div><div class="member-name">Clara Winslow</div><div class="member-role">Chief<br>Talent Acquisition<br>and Culture</div></div>
      <div class="member narrow" style="left:278px;top:90px"><div class="portrait" role="img" aria-label="Portrait of Nina Vale" style="width:76px;height:96px"></div><div class="member-name">Nina Vale</div><div class="member-role">Chief<br>Financial Officer</div></div>
      <div class="member narrow" style="left:377px;top:90px"><div class="portrait" role="img" aria-label="Portrait of Oscar Lindqvist" style="width:76px;height:96px"></div><div class="member-name">Oscar Lindqvist</div><div class="member-role">Director of<br>Advanced Programs</div></div>
      <div class="foot-brand">Kelvoro</div><div class="foot-rule"></div>
      <div class="foot-date">01/07/2024</div><div class="foot-tag">The Global Leader in Forensics, Biometrics, and Identity Intelligence</div><div class="foot-page"><b>20</b> of <b>30</b></div>
    </article>

    <article class="slide" style="left:90px;top:2288px">
      <div class="band"></div>
      <h2 class="heading">Strategic Plans / Graphs</h2>
      <p class="copy" style="width:370px">Lorem ipsum dolor sit amet, consectetuer adipiscing elit, sed diam nonummy nibh euismod tincidunt ut laoreet dolore magna aliquam erat volutpat.</p>
      <svg class="chart" style="position:absolute;left:160px;top:98px" width="126" height="126" viewBox="0 0 126 126">
        <g transform="rotate(-90 63 63)" fill="none" stroke-width="26">
          <circle cx="63" cy="63" r="50" stroke="#2b2a73" stroke-dasharray="110 314"/>
          <circle cx="63" cy="63" r="50" stroke="#a0244f" stroke-dasharray="78 314" stroke-dashoffset="-110"/>
          <circle cx="63" cy="63" r="50" stroke="#b98aa3" stroke-dasharray="69 314" stroke-dashoffset="-188"/>
          <circle cx="63" cy="63" r="50" stroke="#e8ccd7" stroke-dasharray="57 314" stroke-dashoffset="-257"/>
        </g>
      </svg>
      <ul class="legend">
        <li><i style="background:#2b2a73"></i>Objective 1</li>
        <li><i style="background:#a0244f"></i>Objective 2</li>
        <li><i style="background:#b98aa3"></i>Objective 3</li>
        <li><i style="background:#e8ccd7"></i>Objective 4</li>
      </ul>
      <div class="foot-brand">Kelvoro</div><div class="foot-rule"></div>
      <div class="foot-date">01/07/2024</div><div class="foot-tag">The Global Leader in Forensics, Biometrics, and Identity Intelligence</div><div class="foot-page"><b>23</b> of <b>30</b></div>
    </article>

    <article class="slide" style="left:608px;top:2288px">
      <div class="band"></div>
      <h2 class="heading">Contracting with Kelvoro</h2>
      <p class="copy" style="width:200px">Kelvoro holds a variety of IDIQ contracts, including Best-In Class vehicles.</p>
      <ul class="vehicles">
        <li>ORION</li><li>HARBOR – NXG</li><li>FIELD III</li><li>STRIDE</li><li>TASC III</li><li>FSA MAS</li>
      </ul>
      <div class="photo pill-left" role="img" aria-label="Columned government building facade" style="left:295px;top:80px;width:207px;height:140px;background:linear-gradient(100deg,#6d6e70,#b8b7b2 50%,#8a8b8c)"></div>
      <div class="foot-brand">Kelvoro</div><div class="foot-rule"></div>
      <div class="foot-date">01/07/2024</div><div class="foot-tag">The Global Leader in Forensics, Biometrics, and Identity Intelligence</div><div class="foot-page"><b>24</b> of <b>30</b></div>
    </article>

    <article class="slide" style="left:90px;top:2586px">
      <div class="band"></div>
      <h2 class="heading">Careers at Kelvoro</h2>
      <p class="copy">Ready for a challenge? Kelvoro is seeking smart and motivated professionals to work together in pursuit of our noble cause: to build a safe and just world by advancing the science and technologies that identify and protect. Join us in supporting our clients' most critical programs.</p>
      <div class="photo pill-left" role="img" aria-label="Colleagues collaborating in an office" style="left:295px;top:79px;width:207px;height:140px;background:linear-gradient(100deg,#9c9a94,#e4e2dc 50%,#b8b3aa)"></div>
      <div class="foot-brand">Kelvoro</div><div class="foot-rule"></div>
      <div class="foot-date">01/07/2024</div><div class="foot-tag">The Global Leader in Forensics, Biometrics, and Identity Intelligence</div><div class="foot-page"><b>25</b> of <b>30</b></div>
    </article>

    <article class="slide gradient" style="left:608px;top:2586px">
      <div class="cover-brand" style="top:96px">Kelvoro</div>
      <h2 class="cover-title" style="top:158px;font-size:19px">THANK YOU</h2>
      <div class="cover-web" style="left:0;right:0;top:226px;justify-content:center"><i class="dot"></i>www.kelvoro-global.com</div>
    </article>

  </section>
</main>
</body>
</html>
```